Industrial Automation company requires a business card design

Valtrin Automation provides design & build of Automated Equipment for manufacturing industry.
www.valtrinautomation.example
The equipment we design is used for manufacturing in sectors such as medical device, pharmaceutical, aerospace and electronics.
We require a new business card design which incorporates our (New) logo and the key message words:
Automated Equipment:
Design, Build, Control, Test, Support

```html
<!DOCTYPE html>
<html lang="en">
<head>
<meta charset="utf-8">
<title>Valtrin Automation – Business Card</title>
<link href="https://fonts.googleapis.com/css2?family=Source+Sans+3:wght@400;600;700&display=swap" rel="stylesheet">
<style>
  :root {
    --brand-green: #037a3b;
    --map-green: #129050;
    --ink: #231f20;
    --text: #2b2b2b;
    --rule: #9a9a9a;
    --paper: #ffffff;
    --backdrop: #8e8f8f;
  }
  * { margin: 0; padding: 0; box-sizing: border-box; }
  html, body {
    width: 1105px; height: 1200px; overflow: hidden;
    background: var(--backdrop);
    font-family: "Source Sans 3", "Myriad Pro", sans-serif;
  }
  .card { position: absolute; overflow: hidden; }
  .card--front { left: 165px; top: 117px; width: 775px; height: 441px; background: var(--paper); }
  .card--back { left: 166px; top: 631px; width: 773px; height: 443px; background: var(--brand-green); }

  .wordmark {
    position: absolute; display: flex; align-items: center; gap: 10px;
    font-weight: 700; letter-spacing: 0.5px; white-space: nowrap; line-height: 1;
  }
  .wordmark__dot { border-radius: 50%; flex: none; }
  .card--front .wordmark { left: 32px; top: 200px; width: 340px; color: var(--brand-green); font-size: 24px; }
  .card--front .wordmark__dot { width: 32px; height: 32px; background: var(--brand-green); }

  .divider {
    position: absolute; left: 387px; top: 110px; width: 1px; height: 234px; background: var(--rule);
  }
  .contact { position: absolute; left: 416px; top: 104px; color: var(--text); }
  .contact__name { color: var(--brand-green); font-weight: 700; font-size: 23px; line-height: 28px; }
  .contact__role { font-size: 22px; line-height: 28px; }
  .contact__address { margin-top: 14px; font-size: 20px; line-height: 26px; }
  .contact__list { list-style: none; margin-top: 14px; }
  .contact__list li {
    display: flex; align-items: center; gap: 9px; font-size: 20px; line-height: 26.5px;
  }
  .contact__list svg { width: 22px; height: 18px; flex: none; }

  .footer-band { position: absolute; left: 0; bottom: 0; width: 775px; height: 32px; }

  .world-map {
    position: absolute; left: 18px; top: 40px; width: 740px; height: 330px;
    background: radial-gradient(ellipse at 50% 45%, var(--map-green) 0%, #0b8646 50%, var(--brand-green) 72%);
  }
  .card--back .wordmark {
    left: 50%; top: 196px; transform: translateX(-50%);
    color: #ffffff; font-size: 36px; gap: 14px;
  }
  .card--back .wordmark__dot { width: 44px; height: 44px; background: #ffffff; }
  .back-url {
    position: absolute; left: 0; right: 0; top: 393px; text-align: center;
    color: #ffffff; font-size: 20px; letter-spacing: 1.3px;
  }
</style>
</head>
<body>

<section class="card card--front">
  <div class="wordmark">
    <span class="wordmark__dot"></span>
    <span class="wordmark__name">VALTRIN AUTOMATION</span>
  </div>

  <div class="divider"></div>

  <div class="contact">
    <p class="contact__name">DECLAN ARVEY</p>
    <p class="contact__role">CEO</p>
    <p class="contact__address">Glenrath Road, Kilmorna,<br>Co. Westmere, Ireland</p>
    <ul class="contact__list">
      <li>
        <svg viewBox="0 0 22 18" aria-hidden="true"><path fill="#037a3b" d="M2 6c0-3 4-4 9-4s9 1 9 4v1h-5V5H7v2H2zM6 8h10l3 8H3z"/><circle cx="11" cy="12" r="2" fill="#fff"/></svg>
        <span>00 353 (0) 55 01234</span>
      </li>
      <li>
        <svg viewBox="0 0 22 18" aria-hidden="true"><rect x="6" y="1" width="10" height="6" fill="#037a3b"/><rect x="2" y="7" width="18" height="10" rx="2" fill="#037a3b"/><rect x="6" y="11" width="10" height="2" fill="#fff"/></svg>
        <span>00 353 (0) 55 01235</span>
      </li>
      <li>
        <svg viewBox="0 0 22 18" aria-hidden="true"><rect x="1" y="3" width="20" height="13" fill="#037a3b"/><path d="M1 3l10 8 10-8" fill="none" stroke="#fff" stroke-width="1.5"/></svg>
        <span>dwall@valtrin.example</span>
      </li>
      <li>
        <svg viewBox="0 0 22 18" aria-hidden="true"><g fill="none" stroke="#037a3b" stroke-width="1.2"><circle cx="11" cy="9" r="8"/><ellipse cx="11" cy="9" rx="3.5" ry="8"/><path d="M3 9h16M4.5 5h13M4.5 13h13"/></g></svg>
        <span>www.valtrinautomation.example</span>
      </li>
    </ul>
  </div>

  <svg class="footer-band" viewBox="0 0 775 32" aria-hidden="true">
    <rect width="775" height="32" fill="#231f20"/>
    <polygon points="0,0 196,0 228,32 0,32" fill="#037a3b"/>
    <polygon points="196,0 212,0 236,32 220,32" fill="#ffffff"/>
  </svg>
</section>

<section class="card card--back">
  <div class="world-map" role="img" aria-label="Dotted world map background"></div>
  <div class="wordmark">
    <span class="wordmark__dot"></span>
    <span class="wordmark__name">VALTRIN AUTOMATION</span>
  </div>
  <p class="back-url">www.valtrinautomation.example</p>
</section>

</body>
</html>
```